K.E.M.A. The Quillan Orchard Papers

This is the cover artwork for the audio version
of the re-creation of the Quillan Orchard Papers based around the killing of Dorian Vatts. I need a cover for the library binders. I have the template for the binder that I can send. The title of the audio is: K.E.M.A. I would like the words Quillan Orchard Papers added in somehow with some creative graphics. I have a website with other audio covers. I also need the words: Unabridged CD format somewhere at the bottom. Can I send the binder template later?

Target Market(s)

Audiobook

Industry/Entity Type

Audio

Font styles to use
Serif

Requirements
Nice to have
• no bullets, no blood, no dead bodies, no police, no police cars, no protest, no
• violent images, no bullets
Should not have
• nice clear sleek look

```html
<!DOCTYPE html>
<html lang="en">
<head>
<meta charset="utf-8">
<title>K.E.M.A. — Quillan Orchard Papers</title>
<link rel="stylesheet" href="https://fonts.googleapis.com/css2?family=Norican&family=Cormorant+Garamond:wght@600&family=Source+Sans+3:wght@400&display=swap">
<style>
  :root {
    --ember-dark: #1a0904;
    --ember-deep: #5a1606;
    --ember-red: #b8380a;
    --ember-orange: #e9731a;
    --glow-yellow: #ffd84a;
    --glow-core: #fff6c4;
    --ink: #0d0906;
    --title-top: #f7951f;
    --title-bottom: #d8421a;
    --caption: #6f6660;
  }
  html, body {
    margin: 0;
    padding: 0;
    width: 1200px;
    height: 1200px;
    overflow: hidden;
    background: var(--ember-dark);
  }
  .cover {
    position: relative;
    width: 1200px;
    height: 1200px;
    overflow: hidden;
  }
  .cover__glow {
    position: absolute;
    inset: 0;
    background:
      radial-gradient(ellipse 260px 70px at 600px 612px, var(--glow-core) 0%, rgba(255,240,170,0) 100%),
      radial-gradient(ellipse 380px 220px at 640px 470px, var(--glow-yellow) 0%, rgba(255,200,60,0.6) 45%, rgba(255,160,30,0) 100%),
      radial-gradient(ellipse 620px 420px at 600px 470px, var(--ember-orange) 0%, rgba(200,70,15,0.85) 55%, rgba(120,30,8,0) 100%),
      linear-gradient(180deg, var(--ember-deep) 0%, var(--ember-red) 45%, #7a2408 70%, var(--ember-dark) 90%, #0c0604 100%);
  }
  .cover__series {
    position: absolute;
    left: 0;
    right: 0;
    text-align: center;
    font-family: "Norican", cursive;
    color: var(--ink);
    margin: 0;
    font-weight: 400;
  }
  .cover__series--first {
    top: 345px;
    font-size: 104px;
    line-height: 1;
  }
  .cover__series--second {
    top: 482px;
    font-size: 84px;
    line-height: 1;
  }
  .cover__title {
    position: absolute;
    left: 0;
    right: 0;
    top: 760px;
    margin: 0;
    text-align: center;
    font-family: "Cormorant Garamond", serif;
    font-weight: 600;
    font-size: 252px;
    line-height: 1;
    letter-spacing: 4px;
    background: linear-gradient(180deg, var(--title-top) 20%, var(--title-bottom) 80%);
    -webkit-background-clip: text;
    background-clip: text;
    color: transparent;
  }
  .cover__format {
    position: absolute;
    left: 0;
    right: 0;
    top: 1130px;
    margin: 0;
    text-align: center;
    font-family: "Source Sans 3", sans-serif;
    font-size: 22px;
    color: var(--caption);
  }
</style>
</head>
<body>
  <main class="cover">
    <div class="cover__glow" role="img" aria-label="Soft blurred background of glowing orange and yellow firelight fading to dark at the edges"></div>
    <h2 class="cover__series cover__series--first">Quillan</h2>
    <h2 class="cover__series cover__series--second">Orchard Papers</h2>
    <h1 class="cover__title">K.E.M.A.</h1>
    <p class="cover__format">Unabridged CD format</p>
  </main>
</body>
</html>
```